Wine Importer Needs a Wordpress Template

Our company, Corbusan Wine Merchants Ltd, requires a Wordpress template for our new website location (tarnelcask.ie).

We specialise in importing Moldovan wine into Ireland. I have attached a presentation that has background information about the main winery and its wine. I would very much like to see something similar to this in feel and colour. I have also attached our logo which might be useful.

We are very much open to new ideas, so long as the result is something that is clean and easy to use.

Many thanks.
Updates

Project Deadline Extended
Reason: I have extended the deadline by a few days given that I was unable to respond timely to queries. My apologies to all for this. I will be available from now until the new deadline.

Project Deadline Extended

Industry/Entity Type

It Company

```html
<!DOCTYPE html>
<html lang="en">
<head>
<meta charset="utf-8">
<title>Corbusan Wine Merchants Ltd</title>
<link href="https://fonts.googleapis.com/css2?family=Signika:wght@400;600&family=Open+Sans:wght@400;600;700&family=Great+Vibes&display=swap" rel="stylesheet">
<style>
:root{
  --bg:#ece5d5;
  --bg-low:#f1ede4;
  --band:#5a4a3a;
  --green:#1a8a5e;
  --green-dark:#137048;
  --text:#444;
  --muted:#777;
  --white:#fff;
  --tab:#e2ddd0;
  --dark:#3d3d3d;
  --wine:#6a1e3a;
  --orange:#e9a53c;
}
*{margin:0;padding:0;box-sizing:border-box}
html,body{width:720px;height:1200px;overflow:hidden}
body{position:relative;font-family:"Open Sans",Arial,sans-serif;color:var(--text);
  background:linear-gradient(var(--bg) 0,var(--bg) 100px,#e9e3d4 100px,var(--bg-low) 700px,#e4dfd2 1200px)}
.abs{position:absolute}
.top-band{left:0;top:0;width:720px;height:6px;background:var(--band)}
.brand{left:56px;top:20px;width:110px;height:128px;background:var(--white);border-left:3px solid var(--green);
  box-shadow:0 1px 3px rgba(0,0,0,.15);display:flex;flex-direction:column;align-items:center;justify-content:center;gap:6px;text-align:center}
.brand .dot{width:22px;height:22px;border-radius:50%;background:var(--green)}
.brand .name{font-family:Signika,sans-serif;font-size:11px;color:var(--green);line-height:1.25;font-weight:600}
.basket-link{left:515px;top:38px;font-size:8px;color:var(--green)}
.checkout{left:599px;top:38px;width:55px;height:12px;background:var(--green);color:#fff;font-size:7px;font-weight:700;text-align:center;line-height:12px;border-radius:2px}
.contact{left:357px;top:61px;font-size:7.5px;color:var(--text);display:flex;align-items:center;gap:4px}
.basket-note{left:528px;top:60px;font-size:7.5px;color:var(--muted)}
.account{left:357px;top:84px;font-size:6.5px;color:#333}
.nav{top:106px;height:40px;background:var(--tab);padding:10px 0 0 9px}
.nav.active{background:var(--white)}
.nav.home{border-top:3px solid var(--green);padding-top:7px}
.nav b{display:block;font-size:8px;color:#333;font-weight:600}
.nav span{display:block;font-size:6px;color:var(--muted);margin-top:2px}
.card{background:var(--white);box-shadow:0 0 2px rgba(0,0,0,.15)}
.welcome{left:61px;top:157px;width:598px;height:141px;border:1px solid #ccc}
.welcome h1{position:absolute;left:206px;top:25px;font-family:Signika,sans-serif;font-weight:400;font-size:13px;letter-spacing:1px;color:#444}
.welcome .script{position:absolute;left:140px;top:40px;font-family:"Great Vibes",cursive;font-size:20px;color:var(--green);white-space:nowrap}
.welcome p{position:absolute;left:140px;top:74px;width:330px;font-size:6.8px;line-height:12.5px;color:#444}
.more{display:block;color:var(--muted)}
.ph{position:absolute}
.viris{left:60px;top:309px;width:600px;height:210px}
.viris .title{position:absolute;left:244px;top:14px;width:178px;height:27px;border:1px solid #c9b79a;font-family:Signika,sans-serif;font-weight:600;font-size:12px;letter-spacing:1px;color:#333;padding:7px 0 0 17px}
.viris .copy{position:absolute;left:246px;top:48px;width:345px;font-size:6.6px;line-height:12.8px;color:#444}
.viris .copy .g{color:var(--green-dark);margin-top:13px;display:block}
.section-title{left:62px;top:543px;font-family:Signika,sans-serif;font-size:12.5px;font-weight:600;letter-spacing:1px;color:#3b4a55;border-bottom:1px dotted #999;padding-bottom:4px;width:198px}
.tile{overflow:hidden}
.t1{left:65px;top:578px;width:188px;height:263px;background:linear-gradient(#dde6e1,#6fa3a4)}
.t1 h3,.t3 h3{font-family:Signika,sans-serif;font-weight:400;font-size:13px;color:#222}
.t1 h3{position:absolute;left:7px;top:12px}
.t1 p{position:absolute;left:7px;top:42px;width:175px;font-family:Signika,sans-serif;font-size:10px;line-height:13px;color:#222;text-align:justify}
.t1 .warm{position:absolute;left:7px;top:207px;font-family:"Great Vibes",cursive;font-size:13px;color:#222}
.t1 .sel{position:absolute;left:6px;top:228px;font-family:Signika,sans-serif;font-size:12px;letter-spacing:1px;color:#2f5a5c}
.t2{left:266px;width:191px;height:126px}
.t2 .txt{position:absolute;left:102px;top:14px;width:84px;font-size:6.6px;line-height:12.8px}
.t2a{top:578px;background:var(--dark);color:#fff}
.t2b{top:715px;background:#dfe7e0;color:var(--green-dark)}
.t2b .bar{position:absolute;left:0;bottom:0;width:191px;height:14px;background:var(--dark);color:#fff;font-size:6.8px;font-weight:700;padding:3px 0 0 10px}
.t3{left:472px;top:578px;width:187px;height:263px;background:linear-gradient(160deg,#3a1628,var(--wine) 60%,#3e1126)}
.t3 h3{position:absolute;left:8px;top:16px;color:#fff;font-size:13px}
.t3 p{position:absolute;left:13px;top:173px;width:167px;font-family:Signika,sans-serif;font-size:10px;line-height:13px;color:#fff;text-align:justify}
.shop{left:62px;top:857px;width:596px;height:251px;background:var(--white)}
.feature{left:3px;top:6px;width:137px;height:207px;background:linear-gradient(90deg,#f4f2ee,#e7e3dc 55%,#3b0f1a 60%,#2a0b12)}
.feature .lbl{position:absolute;left:5px;background:var(--white);font-family:Signika,sans-serif;font-weight:600;font-size:9.5px;letter-spacing:.6px;color:#222;padding:2px 3px;white-space:nowrap}
.mycart{position:absolute;left:4px;top:224px;width:136px;font-size:7px;color:#333;border-bottom:2px solid #444;padding-bottom:4px}
.vintage-rule{position:absolute;top:19px;height:3px;border-top:1px solid #555;border-bottom:1px solid #555}
.vintage{position:absolute;left:230px;top:6px;width:138px;height:25px;background:var(--green);color:#fff;font-family:Signika,sans-serif;font-weight:600;font-size:11.5px;letter-spacing:.8px;text-align:center;line-height:25px}
.prod-name{position:absolute;font-family:Signika,sans-serif;font-weight:600;font-size:9.5px;letter-spacing:.8px;color:#222;line-height:12px}
.prod-name small{display:block;font-size:8px;font-weight:400;color:var(--green-dark)}
.prod-name i{display:block;font-style:normal;font-size:7px;font-weight:700;color:#222}
.btn{position:absolute;height:18px;border:1px solid #333;font-size:6.5px;text-align:center;line-height:16px;color:#333}
.btn.orange{background:var(--orange);border-color:#c98a2a;color:#fff}
.side-head{position:absolute;left:457px;font-size:7px;color:#222;width:135px;border-bottom:3px double #555;padding-bottom:3px}
.best{position:absolute;left:458px;width:136px;height:40px}
.best .thumb{position:absolute;left:0;top:0;width:36px;height:40px;border:1px solid #ddd;background:linear-gradient(90deg,#fff 35%,#c9a86a 45%,#8a5a2a 55%,#fff 65%)}
.best .nm{position:absolute;left:42px;top:8px;font-family:Signika,sans-serif;font-size:8px;letter-spacing:.6px;color:#2f4f5c}
.best .pr{position:absolute;left:43px;top:19px;font-size:6.5px;font-weight:700;color:#222}
.copyright{left:75px;top:1145px;font-size:7px;color:#222}
.pay{top:1139px;height:11px;border-radius:2px}
</style>
</head>
<body>
<div class="abs top-band"></div>

<div class="abs brand">
  <div class="dot"></div>
  <div class="name">Corbusan Wine<br>Merchants Ltd</div>
</div>

<div class="abs basket-link">View Basket</div>
<div class="abs checkout">Checkout ›</div>
<div class="abs contact">
  <svg width="9" height="7" viewBox="0 0 9 7"><path d="M1 2 Q4.5 -1 8 2 L7 3 L6 2 L3 2 L2 3 Z M2 3.5 H7 L7.5 6.5 H1.5 Z" fill="#333"/></svg>
  020 4410 2736 | Mon-Fri 10am-7pm
</div>
<div class="abs basket-note">Your basket is currently empty.</div>
<div class="abs account">Welcome visitor you can login or create an account &nbsp; Wish List (0) My Account Shopping Cart</div>

<div class="abs nav home" style="left:176px;width:108px"><b>Home</b><span>Find out who we are</span></div>
<div class="abs nav active" style="left:292px;width:116px"><b>Imported</b><span>Selection of our best</span></div>
<div class="abs nav" style="left:415px;width:115px"><b>Production</b><span>Process of getting wine</span></div>
<div class="abs nav" style="left:539px;width:117px"><b>Contact</b><span>Where to find our wines</span></div>

<section class="abs card welcome">
  <div class="ph" role="img" aria-label="Row of wine bottles" style="left:18px;top:22px;width:90px;height:100px;background:linear-gradient(90deg,#fff,#6b4e2e 20%,#2f3a22 40%,#b8a26a 60%,#4a1e22 80%,#fff)"></div>
  <h1>CORBUSAN WINE MERCHANTS</h1>
  <div class="script">Welcome to Corbusan Wine Merchants Limited</div>
  <p>Lorem Ipsum is simply dummy text of the pring and typesetting industry. Lorem Ipsum has been the industry's standard.when an unknownLorem Ipsum has been the industry's standard dummy text....<span class="more">Read More</span></p>
  <div class="ph" role="img" aria-label="Wine glass with dark grapes" style="left:485px;top:40px;width:100px;height:90px;background:radial-gradient(circle at 55% 60%,#1e1e2a 0,#3b4a2a 35%,#9ab86a 55%,#fff 72%)"></div>
</section>

<section class="abs card viris">
  <div class="ph" role="img" aria-label="Bunch of dark grapes under green vine leaves" style="left:0;top:0;width:232px;height:210px;background:radial-gradient(circle at 55% 60%,#2c2a4a 0,#3d3b66 28%,#6f9a2e 45%,#a8c860 65%,#fff 82%)"></div>
  <div class="title">VIRIS FUISSET INSOLI</div>
  <div class="copy">Lorem Ipsum is simply dummy text of the pring and typesetting industry. Lorem Ipsum has been the industry's standard.when an unknownLorem Ipsum has been the industry's standard dummy text.... Sed ut perspiciatis unde omnis iste natus error sit voluptatem accusantium doloremque laudantium, totam rem aperiam, eaque ipsa quae ab illo inventore veritatis et quasi archite... Donec tellus Nulla lorem Nullam elit id ut elit feugiat lacus. Congue eget dapibus congue tincidunt senectus nibh risus Phasellus tristique justo. Justo Pellentesque Donec lobor...
    <span class="g">Donec tellus Nulla lorem Nullam elit id ut elit feugiat lacus. Congue eget dapibus congue tincidunt senectus nibh risus Phasellus tristique justo. Justo Pellentesque Donec lobor...</span>
    <span class="more" style="margin-top:4px">Read More</span>
  </div>
</section>

<h2 class="abs section-title">WINE SELECTION 2014</h2>

<div class="abs tile t1">
  <h3>Ridens tacimates</h3>
  <p>Vivendum disputando adversarium nec ea, an mel paulo vituperata. Hinc part em aliquam te qui. Ne nobis delectus mentum ne qui...</p>
  <div class="ph" role="img" aria-label="Five red wine bottles" style="left:40px;top:122px;width:125px;height:80px;background:linear-gradient(90deg,transparent,#7a1e22 10%,#e8e0cc 30%,#7a1e22 50%,#e8e0cc 70%,#7a1e22 90%,transparent)"></div>
  <div class="warm">Warm</div>
  <div class="sel">WINE SELECTION 2014</div>
</div>

<div class="abs tile t2 t2a">
  <div class="ph" role="img" aria-label="Three sparkling wine bottles" style="left:18px;top:18px;width:80px;height:92px;background:linear-gradient(90deg,transparent 5%,#2a3a2a 15%,#c9b070 25%,transparent 33%,#1e2a1e 45%,transparent 58%,#3f8a3a 70%,#d8c27a 80%,transparent 92%)"></div>
  <div class="txt">Lorem Ipsum is simply dummy text of the pring and typesetting industry. Lorem Ipsum has been the industry's<br><b style="display:block;margin-top:10px">Curabitur vitaes a lorem Nullam elit</b></div>
</div>

<div class="abs tile t2 t2b">
  <div class="ph" role="img" aria-label="Three sparkling wine bottles" style="left:10px;top:8px;width:88px;height:96px;background:linear-gradient(90deg,transparent 5%,#2a3a2a 15%,#c9b070 25%,transparent 33%,#1e2a1e 45%,transparent 58%,#3f8a3a 70%,#d8c27a 80%,transparent 92%)"></div>
  <div class="txt" style="top:12px">Lorem Ipsum is simply dummy text of the pring and typesetting industry. Lorem Ipsum has been the industry's<br><i style="display:block">Curabitur vitaes a lorem Nullam elit id</i></div>
  <div class="bar">Curabitur vitaes lorem Nullam elit id ut</div>
</div>

<div class="abs tile t3" role="img" aria-label="Glass of red wine beside a bottle">
  <h3>Ridens tacimates</h3>
  <p>Vivendum disputando adversarium nec ea, an mel paulo vituperata. Hinc part em aliquam te qui. Ne nobis delectus mentum ne qui...</p>
</div>

<section class="abs shop">
  <div class="ph feature" role="img" aria-label="Bottle and label of a red anniversary edition wine">
    <span class="lbl" style="top:40px">NEGRUDE</span>
    <span class="lbl" style="top:59px">TARNELANNIVERSARY</span>
    <span class="lbl" style="top:78px">EDITION,</span>
    <span class="lbl" style="top:97px">VINTAGE 2009</span>
  </div>
  <div class="mycart">MY CART</div>

  <div class="vintage-rule" style="left:162px;width:68px"></div>
  <div class="vintage">VINTAGE COLLECTION</div>
  <div class="vintage-rule" style="left:368px;width:68px"></div>

  <div class="ph" role="img" aria-label="Rosé wine bottle label" style="left:168px;top:48px;width:120px;height:132px;border:1px solid #ccc;background:linear-gradient(#fff 55%,#3a0d14 80%,#1a0508)"></div>
  <div class="prod-name" style="left:181px;top:186px">ROŞUDE TARNEL,<small>WINE SELECTION</small><i>$ 250.00</i></div>
  <div class="btn" style="left:174px;top:222px;width:67px">ADD TO CART</div>
  <div class="btn" style="left:244px;top:222px;width:19px">★</div>
  <div class="btn" style="left:266px;top:222px;width:19px">❐</div>

  <div class="ph" role="img" aria-label="Oak barrel with wine glass and grapes" style="left:307px;top:48px;width:122px;height:132px;background:linear-gradient(135deg,#3a2618,#7a5434 45%,#c9b682 70%,#4a3420)"></div>
  <div class="prod-name" style="left:314px;top:186px">ROŞUDE TARNEL,<small>WINE SELECTION</small><i>$ 250.00</i></div>
  <div class="btn orange" style="left:311px;top:222px;width:67px">ADD TO CART</div>
  <div class="btn orange" style="left:381px;top:222px;width:19px">★</div>
  <div class="btn orange" style="left:403px;top:222px;width:19px">❐</div>

  <div class="side-head" style="top:8px">BEST SELLER</div>
  <div class="best" style="top:35px"><div class="thumb" role="img" aria-label="Wine bottle"></div><div class="nm">WINE SELECTION</div><div class="pr">$ 250.00</div></div>
  <div class="best" style="top:87px"><div class="thumb" role="img" aria-label="Wine bottle"></div><div class="nm">WINE SELECTION</div><div class="pr">$ 250.00</div></div>
  <div class="best" style="top:136px"><div class="thumb" role="img" aria-label="Wine bottle"></div><div class="nm">WINE SELECTION</div><div class="pr">$ 250.00</div></div>
  <div class="best" style="top:184px"><div class="thumb" role="img" aria-label="Wine bottle"></div><div class="nm">WINE SELECTION</div><div class="pr">$ 250.00</div></div>
  <div class="side-head" style="top:231px;border:none">MOST VIEWED</div>
</section>

<div class="abs copyright">Copyright © 2012. All Rights Reserved Corbusan Wine Merchants</div>
<div class="abs pay" style="left:496px;width:20px;background:#2b4a9a"></div>
<div class="abs pay" style="left:520px;width:14px;background:#c8462e"></div>
<div class="abs pay" style="left:538px;width:14px;background:#2b4a9a"></div>
<div class="abs pay" style="left:556px;width:14px;background:#4a8ac8"></div>
<div class="abs pay" style="left:574px;width:12px;background:#1e3a7a;border-radius:50%"></div>
<div class="abs pay" style="left:590px;width:26px;background:#3a6ac8"></div>
<div class="abs pay" style="left:621px;width:26px;border:1px solid #c8462e"></div>
</body>
</html>
```